Turn this into a clear and concise

Attached is a screen shot that we currently show to investors from a software program. We need you to illustrate this in a much more professional looking and easy to view and understand way. If we like your style and attention to detail there is more work behind this.
Industry/Entity Type
Software

```html
<!DOCTYPE html>
<html lang="en">
<head>
<meta charset="utf-8">
<title>Intraday Price, Momentum and Volume</title>
<link href="https://fonts.googleapis.com/css2?family=Carlito:wght@400;700&display=swap" rel="stylesheet">
<style>
  :root{
    --bg:#f7f4ef;
    --axis:#5f7f84;
    --grid:#e6e3de;
    --label:#4a4a4a;
    --up:#b5cc12;
    --down:#e0622a;
    --wick:#e98a5a;
    --resist:#e98a5a;
    --target:#c9d46a;
    --volume:#1ccfcf;
  }
  html,body{margin:0;padding:0;overflow:hidden;background:var(--bg);}
  .chart{display:block;width:1200px;height:1120px;font-family:"Carlito",sans-serif;}
  .grid line{stroke:var(--grid);stroke-width:1.5;}
  .axis{stroke:var(--axis);fill:none;}
  .label{fill:var(--label);font-weight:700;font-size:25px;}
  .label-sm{fill:var(--label);font-weight:700;font-size:11px;}
  .label-time{fill:var(--label);font-weight:700;font-size:31px;text-anchor:middle;}
  .resistance{stroke:var(--resist);stroke-width:1.5;}
  .target{stroke:var(--target);stroke-width:1;stroke-dasharray:2 2;}
  .target.grey{stroke:#c8c4bd;}
  .wick{stroke:var(--wick);stroke-width:1.5;}
  .up{fill:var(--up);stroke:var(--wick);stroke-width:1;}
  .down{fill:var(--down);stroke:var(--down);stroke-width:1;}
  .signal{fill:var(--down);}
  .momentum{fill:none;stroke:var(--up);stroke-width:3;stroke-linejoin:round;}
  .volume rect{fill:var(--volume);}
</style>
</head>
<body>
<svg class="chart" viewBox="0 0 1200 1120" xmlns="http://www.w3.org/2000/svg">
  <g class="grid">
    <line x1="322" y1="215" x2="322" y2="965"/>
    <line x1="506" y1="215" x2="506" y2="965"/>
    <line x1="690" y1="215" x2="690" y2="965"/>
    <line x1="875" y1="215" x2="875" y2="965"/>
    <line x1="166" y1="316" x2="990" y2="316"/>
    <line x1="166" y1="407" x2="990" y2="407"/>
    <line x1="166" y1="498" x2="990" y2="498"/>
    <line x1="166" y1="537" x2="990" y2="537"/>
    <line x1="166" y1="583" x2="990" y2="583"/>
    <line x1="166" y1="758" x2="990" y2="758"/>
    <line x1="166" y1="833" x2="990" y2="833"/>
    <line x1="166" y1="900" x2="990" y2="900"/>
  </g>

  <line class="resistance" x1="166" y1="179" x2="990" y2="179"/>
  <g class="targets">
    <line class="target" x1="170" y1="233" x2="990" y2="233"/>
    <line class="target" x1="170" y1="246" x2="990" y2="246"/>
    <line class="target grey" x1="170" y1="259" x2="990" y2="259"/>
    <line class="target grey" x1="170" y1="271" x2="990" y2="271"/>
    <line class="target" x1="170" y1="283" x2="990" y2="283"/>
  </g>

  <g class="candles">
    <rect class="down" x="258" y="270" width="8" height="9"/>
    <line class="wick" x1="275" y1="279" x2="275" y2="300"/><rect class="down" x="270" y="279" width="10" height="21"/>
    <line class="wick" x1="292" y1="300" x2="292" y2="322"/><rect class="down" x="287" y="300" width="10" height="8"/>
    <line class="wick" x1="301" y1="308" x2="311" y2="308"/>
    <line class="wick" x1="320" y1="304" x2="320" y2="315"/><line class="wick" x1="315" y1="308" x2="325" y2="308"/>
    <rect class="up" x="331" y="300" width="10" height="8"/>
    <line class="wick" x1="349" y1="293" x2="349" y2="302"/><line class="wick" x1="344" y1="298" x2="354" y2="298"/>
    <rect class="down" x="359" y="300" width="10" height="8"/>
    <line class="wick" x1="379" y1="309" x2="379" y2="322"/><line class="wick" x1="374" y1="315" x2="384" y2="315"/>
    <line class="wick" x1="392" y1="309" x2="392" y2="322"/><line class="wick" x1="387" y1="315" x2="397" y2="315"/>
    <line class="wick" x1="408" y1="309" x2="408" y2="337"/><rect class="down" x="403" y="323" width="10" height="7"/>
    <line class="wick" x1="423" y1="325" x2="423" y2="370"/><rect class="down" x="418" y="330" width="10" height="37"/>
    <line class="wick" x1="437" y1="368" x2="437" y2="380"/><rect class="down" x="432" y="368" width="10" height="7"/>
    <line class="wick" x1="452" y1="378" x2="452" y2="466"/><rect class="down" x="447" y="385" width="10" height="45"/>
    <line class="wick" x1="467" y1="430" x2="467" y2="480"/><rect class="down" x="462" y="436" width="10" height="22"/>
    <line class="wick" x1="482" y1="450" x2="482" y2="513"/><line class="wick" x1="477" y1="455" x2="487" y2="455"/>
    <line class="wick" x1="495" y1="458" x2="495" y2="465"/><rect class="up" x="490" y="429" width="10" height="29"/>
    <line class="wick" x1="511" y1="420" x2="511" y2="445"/><line class="wick" x1="506" y1="428" x2="516" y2="428"/>
    <rect class="up" x="520" y="421" width="10" height="8"/>
    <line class="wick" x1="540" y1="413" x2="540" y2="429"/><rect class="up" x="535" y="421" width="10" height="8"/>
    <line class="wick" x1="555" y1="400" x2="555" y2="420"/><rect class="up" x="550" y="405" width="10" height="15"/>
    <line class="wick" x1="568" y1="392" x2="568" y2="413"/><line class="wick" x1="563" y1="405" x2="573" y2="405"/>
    <rect class="down" x="578" y="405" width="10" height="15"/>
    <line class="wick" x1="598" y1="414" x2="598" y2="428"/><line class="wick" x1="593" y1="420" x2="603" y2="420"/>
    <line class="wick" x1="612" y1="413" x2="612" y2="427"/><rect class="up" x="607" y="413" width="10" height="7"/>
    <line class="wick" x1="628" y1="398" x2="628" y2="420"/><rect class="up" x="623" y="398" width="10" height="15"/>
    <line class="wick" x1="643" y1="390" x2="643" y2="405"/><line class="wick" x1="638" y1="398" x2="648" y2="398"/>
    <line class="wick" x1="657" y1="352" x2="657" y2="420"/><rect class="up" x="652" y="360" width="10" height="38"/>
    <line class="wick" x1="672" y1="348" x2="672" y2="375"/><rect class="up" x="667" y="353" width="10" height="15"/>
    <rect class="down" x="682" y="353" width="10" height="7"/>
    <line class="wick" x1="701" y1="353" x2="701" y2="390"/><rect class="down" x="696" y="353" width="10" height="30"/>
    <line class="wick" x1="715" y1="378" x2="715" y2="420"/><rect class="down" x="710" y="383" width="10" height="15"/>
    <line class="wick" x1="731" y1="375" x2="731" y2="405"/><rect class="up" x="726" y="375" width="10" height="23"/>
    <line class="wick" x1="744" y1="375" x2="744" y2="392"/><line class="wick" x1="739" y1="383" x2="749" y2="383"/>
    <line class="wick" x1="759" y1="375" x2="759" y2="398"/><line class="wick" x1="754" y1="383" x2="764" y2="383"/>
    <line class="wick" x1="774" y1="360" x2="774" y2="390"/><rect class="up" x="769" y="368" width="10" height="15"/>
    <line class="wick" x1="788" y1="353" x2="788" y2="383"/><rect class="up" x="783" y="353" width="10" height="22"/>
    <rect class="up" x="798" y="330" width="10" height="23"/>
    <rect class="down" x="813" y="330" width="10" height="23"/>
    <rect class="up" x="827" y="346" width="10" height="7"/>
    <line class="wick" x1="847" y1="338" x2="847" y2="353"/><line class="wick" x1="842" y1="345" x2="852" y2="345"/>
    <line class="wick" x1="862" y1="316" x2="862" y2="346"/><rect class="up" x="857" y="323" width="10" height="23"/>
    <line class="wick" x1="876" y1="296" x2="876" y2="322"/><rect class="up" x="871" y="301" width="10" height="15"/>
    <line class="wick" x1="889" y1="295" x2="889" y2="307"/><line class="wick" x1="884" y1="300" x2="894" y2="300"/>
  </g>

  <g class="signal-arrow">
    <rect class="signal" x="871" y="249" width="9" height="16"/>
    <polygon class="signal" points="865,265 886,265 875.5,276"/>
  </g>

  <line class="axis" x1="166" y1="705" x2="990" y2="705" stroke-width="2"/>
  <polyline class="momentum" points="259,681 275,718 287,725 320,726 337,683 350,687 373,713 397,716 421,748 434,748 451,753 483,755 493,691 511,691 527,673 539,673 555,635 567,637 582,673 598,673 624,616 645,612 655,575 672,568 689,592 701,652 714,669 734,631 745,647 762,646 802,574 820,630 832,618 850,618 870,578 889,575"/>

  <g class="volume">
    <rect x="226" y="957" width="8" height="8"/><rect x="240" y="935" width="8" height="30"/>
    <rect x="255" y="945" width="8" height="20"/><rect x="271" y="950" width="8" height="15"/>
    <rect x="286" y="957" width="8" height="8"/><rect x="302" y="956" width="8" height="9"/>
    <rect x="332" y="948" width="8" height="17"/><rect x="348" y="948" width="8" height="17"/>
    <rect x="364" y="951" width="8" height="14"/><rect x="378" y="921" width="8" height="44"/>
    <rect x="394" y="908" width="8" height="57"/><rect x="409" y="926" width="8" height="39"/>
    <rect x="423" y="822" width="8" height="143"/><rect x="440" y="878" width="8" height="87"/>
    <rect x="455" y="843" width="8" height="122"/><rect x="471" y="905" width="8" height="60"/>
    <rect x="486" y="912" width="8" height="53"/><rect x="502" y="938" width="8" height="27"/>
    <rect x="517" y="941" width="8" height="24"/><rect x="533" y="918" width="8" height="47"/>
    <rect x="547" y="925" width="8" height="40"/><rect x="563" y="944" width="8" height="21"/>
    <rect x="578" y="955" width="8" height="10"/><rect x="594" y="951" width="8" height="14"/>
    <rect x="608" y="935" width="8" height="30"/><rect x="625" y="942" width="8" height="23"/>
    <rect x="640" y="884" width="8" height="81"/><rect x="655" y="919" width="8" height="46"/>
    <rect x="671" y="926" width="8" height="39"/><rect x="686" y="949" width="8" height="16"/>
    <rect x="702" y="915" width="8" height="50"/><rect x="718" y="934" width="8" height="31"/>
    <rect x="732" y="932" width="8" height="33"/><rect x="748" y="940" width="8" height="25"/>
    <rect x="764" y="940" width="8" height="25"/><rect x="778" y="933" width="8" height="32"/>
    <rect x="794" y="926" width="8" height="39"/><rect x="809" y="945" width="8" height="20"/>
    <rect x="825" y="931" width="8" height="34"/><rect x="840" y="935" width="8" height="30"/>
    <rect x="856" y="918" width="8" height="47"/><rect x="872" y="926" width="8" height="39"/>
    <rect x="886" y="947" width="8" height="18"/>
  </g>
  <line class="axis" x1="166" y1="966" x2="992" y2="966" stroke-width="3"/>

  <line class="axis" x1="995" y1="110" x2="995" y2="1013" stroke-width="9"/>
  <polyline class="axis" points="970,144 995,108 1020,144" stroke-width="9"/>

  <g class="price-labels">
    <text class="label" x="1008" y="199">137’24</text>
    <text class="label-sm" x="1010" y="237">137’20</text>
    <text class="label-sm" x="1010" y="250">137’18</text>
    <text class="label-sm" x="1010" y="263">137’16</text>
    <text class="label-sm" x="1010" y="276">137’14</text>
    <text class="label-sm" x="1010" y="288">137’12</text>
    <text class="label" x="1008" y="328">137’08</text>
    <text class="label" x="1008" y="419">136’28</text>
    <text class="label" x="1008" y="511">136’16</text>
    <text class="label" x="1008" y="546">100</text>
    <text class="label" x="1008" y="768">0</text>
    <text class="label" x="1008" y="842">20,000</text>
    <text class="label" x="1008" y="909">10,000</text>
  </g>
  <g class="time-labels">
    <text class="label-time" x="327" y="1008">8am</text>
    <text class="label-time" x="506" y="1008">9am</text>
    <text class="label-time" x="690" y="1008">10am</text>
    <text class="label-time" x="877" y="1008">11am</text>
  </g>
</svg>
</body>
</html>
```